依頼詳細
毎年クリスマスカードと(2014)年賀状(2015)をあわせてご挨拶含めカードをお客様へお送りするはがきの表面のデザインをお願い致します。クリスマスメインで欲しいです。素敵なデザイン(写真可)をお願いします。
記載項目
会社ロゴ(石垣設計社)HAPPY WINTER GREETINGS 2014-2015
希望イメージ
シンプル 複雑
単色 カラフル
暗い 明るい
日常 高級
遊び心 厳粛
未来的 伝統的
女性的 男性的
希望する色
赤系、青系、水色系、茶系、緑系、黄・オレンジ系、グレー系
納品ファイル
• イラストレーター形式 (.ai)
補足説明
柔軟なアイデアを募集しております。
写真を使ってカードをデザインして下さい。
クリスマス前にお送りしますので、クリスマス使用にして欲しいです。
■ 選んだ理由

家と家具(いす)雑貨などそれぞれの素材を活かし、且つ温かさとぬくもりを感じる作品のご提案をいただけたことです。

■ 提案者全員のお礼・コメント

ご提案ありがとうございました。
素材でお送りした写真を上手く活用していただけ、幅広いご提案をいただけたこと、アイデアにとても感謝しております。
ありがとうございました。
すばらしい作品ばかりご応募いただけ、依頼して良かったと思っております。
また、機会がありましたらぜひ、ご協力いただきたいと思います。
ありがとうございました。

```html
<!DOCTYPE html>
<html lang="ja">
<head>
<meta charset="utf-8">
<title>Happy Winter Greetings 2014-2015</title>
<link rel="stylesheet" href="https://fonts.googleapis.com/css2?family=Great+Vibes&family=Montserrat:wght@700&family=Noto+Sans+JP:wght@500&display=swap">
<style>
  :root {
    --paper: #ffffff;
    --script-red: #8c2f3b;
    --photo-light: #f6ecd2;
    --photo-mid: #e9c48a;
    --photo-warm: #e39a4a;
    --mullion: #ffffff;
    --year-pale: #d8c29c;
    --year-orange: #e58a2c;
    --year-deep: #c86a22;
    --name-ink: #6b4a3a;
    --snow: #d5dde6;
  }
  html, body {
    margin: 0;
    padding: 0;
    overflow: hidden;
    background: var(--paper);
  }
  .card {
    position: relative;
    width: 809px;
    height: 1200px;
    background: var(--paper);
    overflow: hidden;
  }
  .greeting {
    position: absolute;
    top: 70px;
    left: 0;
    width: 100%;
    margin: 0;
    text-align: center;
    font-family: "Great Vibes", cursive;
    font-weight: 400;
    font-size: 88px;
    line-height: 94px;
    color: var(--script-red);
  }
  .window {
    position: absolute;
    left: 192px;
    top: 324px;
    width: 434px;
    height: 580px;
    border-radius: 217px 217px 0 0;
    overflow: hidden;
    background: linear-gradient(180deg, var(--photo-light) 0%, var(--photo-mid) 45%, var(--photo-warm) 100%);
  }
  .mullion-vertical {
    position: absolute;
    left: 213px;
    top: 0;
    width: 8px;
    height: 100%;
    background: var(--mullion);
  }
  .mullion-horizontal {
    position: absolute;
    left: 0;
    top: 315px;
    width: 100%;
    height: 8px;
    background: var(--mullion);
  }
  .snowflake {
    position: absolute;
    border-radius: 50%;
    background: var(--snow);
    opacity: 0.55;
  }
  .years {
    position: absolute;
    top: 906px;
    left: 0;
    width: 100%;
    margin: 0;
    text-align: center;
    font-family: "Montserrat", sans-serif;
    font-weight: 700;
    font-size: 90px;
    line-height: 100px;
    letter-spacing: -1px;
    color: var(--year-deep);
  }
  .years .pale { color: var(--year-pale); }
  .years .accent { color: var(--year-orange); }
  .company {
    position: absolute;
    top: 1088px;
    left: 0;
    width: 100%;
    margin: 0;
    text-align: center;
    font-family: "Noto Sans JP", sans-serif;
    font-weight: 500;
    font-size: 22px;
    line-height: 30px;
    letter-spacing: 4px;
    color: var(--name-ink);
  }
</style>
</head>
<body>
  <main class="card">
    <h1 class="greeting">Happy Winter<br>Greetings</h1>

    <div class="snowflake" role="img" aria-label="Snowflake decoration" style="left:50px; top:225px; width:50px; height:50px;"></div>
    <div class="snowflake" role="img" aria-label="Snowflake decoration" style="left:105px; top:275px; width:85px; height:85px;"></div>
    <div class="snowflake" role="img" aria-label="Snowflake decoration" style="left:95px; top:395px; width:36px; height:36px;"></div>
    <div class="snowflake" role="img" aria-label="Snowflake decoration" style="left:595px; top:405px; width:130px; height:130px;"></div>
    <div class="snowflake" role="img" aria-label="Snowflake decoration" style="left:720px; top:550px; width:40px; height:40px;"></div>
    <div class="snowflake" role="img" aria-label="Snowflake decoration" style="left:690px; top:975px; width:70px; height:70px;"></div>
    <div class="snowflake" role="img" aria-label="Snowflake decoration" style="left:625px; top:1080px; width:45px; height:45px;"></div>

    <div class="window" role="img" aria-label="Warm interior photo seen through an arched window: shelves with bottles and books, a desk lamp and an open magazine on a wooden desk">
      <div class="mullion-vertical"></div>
      <div class="mullion-horizontal"></div>
    </div>

    <p class="years"><span class="pale">201</span><span class="accent">4</span>-2015</p>

    <p class="company">石垣設計社</p>
  </main>
</body>
</html>
```